Marvane Painting Epoxy Flyer

We need a promotional flyer for a new epoxy floor coatings division of our painting company. We do epoxy garage floor coatings and paver sealing. It needs to be based on and very similar to the attached flyer. The garage floor picture needs to look more realistic, and the before and after pavers pictures should look less shiny but still a good contrast. Include attached logo

```html
<!DOCTYPE html>
<html lang="en">
<head>
<meta charset="utf-8">
<title>Marvane Painting – Garage & Driveway Flyer</title>
<link rel="stylesheet" href="https://fonts.googleapis.com/css2?family=Krona+One&family=Exo+2:wght@400;500&family=Poppins:wght@400;500;600;700;800&display=swap">
<style>
  :root {
    --navy-light: #33447a;
    --navy: #222c55;
    --navy-dark: #121831;
    --white: #ffffff;
    --blue: #1fa5dc;
    --green: #4fbf2c;
    --orange: #c97a1c;
    --orange-text: #d4831f;
    --line: rgba(255,255,255,0.75);
    --stage: #bcbcbc;
  }
  * { box-sizing: border-box; margin: 0; padding: 0; }
  html, body {
    width: 1043px; height: 1200px; overflow: hidden;
    background: var(--stage);
    font-family: "Poppins", sans-serif;
  }
  .flyer {
    position: absolute; left: 57px; top: 0;
    width: 928px; height: 1200px; overflow: hidden;
    background: radial-gradient(ellipse 70% 55% at 45% 48%, var(--navy-light) 0%, var(--navy) 50%, var(--navy-dark) 100%);
    color: var(--white);
  }
  .abs { position: absolute; }

  /* top photo pair */
  .photo-pair {
    left: 48px; top: 117px; width: 829px; height: 315px;
  }
  .photo-frame {
    position: absolute; top: 0; height: 315px;
    border: 6px solid var(--white); border-radius: 8px; overflow: hidden;
  }
  .photo-frame.left { left: 0; width: 414px; }
  .photo-frame.right { left: 418px; width: 411px; }
  .photo { width: 100%; height: 100%; }
  .garage-before {
    background: linear-gradient(180deg, #8f8e86 0%, #a7a69d 32%, #d8d6cc 44%, #6d6a5f 52%, #4a473e 100%);
  }
  .garage-after {
    background: linear-gradient(180deg, #b9b6ab 0%, #d4d1c7 32%, #f1efe8 44%, #8c897f 53%, #6c6960 100%);
  }

  .tag {
    position: absolute; width: 150px; height: 37px;
    display: flex; align-items: center; justify-content: center;
    font-weight: 700; font-size: 21px; letter-spacing: 0.5px; color: var(--white);
    border-radius: 2px;
  }
  .tag.before { background: var(--green); }
  .tag.after { background: var(--blue); }

  /* brand mark */
  .brand-disc {
    left: 375px; top: 33px; width: 178px; height: 178px; border-radius: 50%;
    background: var(--navy);
  }
  .brand-name {
    left: 344px; top: 103px; width: 240px; height: 28px;
    background: #e9e9e9; color: var(--navy-dark);
    display: flex; align-items: center; justify-content: center;
    font-weight: 600; font-size: 17px; letter-spacing: 0.2px;
  }

  /* headline */
  .headline { left: 48px; top: 478px; width: 520px; }
  .headline .kicker {
    font-family: "Exo 2", sans-serif; font-weight: 400;
    font-size: 55px; line-height: 62px; color: var(--blue);
  }
  .headline .main {
    font-family: "Krona One", sans-serif; font-size: 66px; line-height: 78px;
    letter-spacing: -1px; color: var(--white);
  }
  .headline-rule {
    left: 48px; top: 694px; width: 426px; height: 1px; background: rgba(255,255,255,0.5);
  }
  .tagline {
    left: 49px; top: 702px;
    font-family: "Exo 2", sans-serif; font-weight: 500;
    font-size: 35px; color: var(--orange-text);
  }

  /* service tables */
  .service {
    top: 753px; width: 235px; height: 235px;
    border: 1.5px solid var(--line); border-radius: 5px;
    display: flex; flex-direction: column;
  }
  .service.epoxy { left: 48px; }
  .service.pavers { left: 299px; }
  .service h3 {
    height: 46px; display: flex; align-items: center; padding-left: 14px;
    font-size: 14px; font-weight: 700; letter-spacing: 0.2px;
    border-bottom: 1.5px solid var(--line);
  }
  .service.epoxy h3 { color: var(--green); }
  .service.pavers h3 { color: var(--blue); padding-left: 8px; }
  .service ul { list-style: none; flex: 1; display: flex; flex-direction: column; }
  .service li {
    flex: 1; display: flex; align-items: center; gap: 7px;
    padding-left: 15px; padding-right: 6px;
    font-size: 12.4px; line-height: 15px;
    border-bottom: 1.5px solid var(--line);
  }
  .service.pavers li { padding-left: 10px; }
  .service li:last-child { border-bottom: none; }
  .dot { flex: none; width: 7px; height: 7px; }

  /* room photos */
  .room-panel {
    left: 594px; top: 501px; width: 273px; height: 471px;
    border: 5px solid var(--white); border-radius: 6px; overflow: hidden;
    background: var(--white); display: flex; flex-direction: column; gap: 5px;
  }
  .room-panel .photo { flex: 1; }
  .room-before {
    background: linear-gradient(180deg, #e8e6e2 0%, #dcd9d3 58%, #8b7058 62%, #6e523c 100%);
  }
  .room-after {
    background: linear-gradient(180deg, #ecebe7 0%, #d9d6cf 58%, #7a6550 63%, #4f4134 100%);
  }

  /* trust row */
  .trust-title {
    left: 48px; top: 1017px; font-size: 14.5px; font-weight: 700; letter-spacing: 0.1px;
  }
  .trust-item {
    top: 1047px; width: 170px; text-align: center;
    font-size: 12.4px; line-height: 15px;
  }
  .trust-item svg { display: block; margin: 0 auto 6px; }
  .trust-divider { top: 1050px; width: 1px; height: 82px; background: rgba(255,255,255,0.45); }

  /* call to action */
  .cta {
    left: 591px; top: 1016px; width: 278px; height: 82px;
    background: var(--orange); border: 1px solid #e0a04e;
    display: flex; flex-direction: column; align-items: center; justify-content: center;
  }
  .cta .label { font-size: 18px; font-weight: 500; letter-spacing: 0.6px; line-height: 22px; }
  .cta .phone { font-size: 36px; font-weight: 800; line-height: 40px; letter-spacing: 0.5px; }
  .cta-note {
    left: 588px; top: 1104px; width: 284px; text-align: center;
    font-size: 13.5px; font-weight: 700;
  }
</style>
</head>
<body>
<main class="flyer">

  <section class="photo-pair abs">
    <div class="photo-frame left">
      <div class="photo garage-before" role="img" aria-label="Worn concrete garage floor before coating"></div>
    </div>
    <div class="photo-frame right">
      <div class="photo garage-after" role="img" aria-label="Clean coated garage floor after epoxy"></div>
    </div>
    <div class="tag before" style="left:126px; top:297px;">BEFORE</div>
    <div class="tag after" style="left:548px; top:297px;">AFTER</div>
  </section>

  <div class="brand-disc abs"></div>
  <div class="brand-name abs">Marvane Painting</div>

  <div class="headline abs">
    <div class="kicker">Upgrade Your</div>
    <div class="main">Garage &amp;<br>Driveway</div>
  </div>
  <div class="headline-rule abs"></div>
  <div class="tagline abs">From worn-out to like new</div>

  <section class="service epoxy abs">
    <h3>EPOXY FLOOR COATINGS</h3>
    <ul>
      <li><svg class="dot" viewBox="0 0 8 8"><circle cx="4" cy="4" r="4" fill="#4fbf2c"/><path d="M2.2 4.1 3.5 5.3 5.9 2.8" stroke="#121831" stroke-width="1.1" fill="none"/></svg>Durable, long-lasting finish</li>
      <li><svg class="dot" viewBox="0 0 8 8"><circle cx="4" cy="4" r="4" fill="#4fbf2c"/><path d="M2.2 4.1 3.5 5.3 5.9 2.8" stroke="#121831" stroke-width="1.1" fill="none"/></svg>Slip-resistant texture</li>
      <li><svg class="dot" viewBox="0 0 8 8"><circle cx="4" cy="4" r="4" fill="#4fbf2c"/><path d="M2.2 4.1 3.5 5.3 5.9 2.8" stroke="#121831" stroke-width="1.1" fill="none"/></svg>Covers cracks &amp; imperfections</li>
      <li><svg class="dot" viewBox="0 0 8 8"><circle cx="4" cy="4" r="4" fill="#4fbf2c"/><path d="M2.2 4.1 3.5 5.3 5.9 2.8" stroke="#121831" stroke-width="1.1" fill="none"/></svg>Easy to clean &amp; maintain</li>
    </ul>
  </section>

  <section class="service pavers abs">
    <h3>PAVER SEALING</h3>
    <ul>
      <li><svg class="dot" viewBox="0 0 8 8"><circle cx="4" cy="4" r="4" fill="#1fa5dc"/><path d="M2.2 4.1 3.5 5.3 5.9 2.8" stroke="#121831" stroke-width="1.1" fill="none"/></svg>Restores color &amp;<br>enhances appearance</li>
      <li><svg class="dot" viewBox="0 0 8 8"><circle cx="4" cy="4" r="4" fill="#1fa5dc"/><path d="M2.2 4.1 3.5 5.3 5.9 2.8" stroke="#121831" stroke-width="1.1" fill="none"/></svg>Protects from sun fading</li>
      <li><svg class="dot" viewBox="0 0 8 8"><circle cx="4" cy="4" r="4" fill="#1fa5dc"/><path d="M2.2 4.1 3.5 5.3 5.9 2.8" stroke="#121831" stroke-width="1.1" fill="none"/></svg>Helps prevent weeds &amp; sand loss</li>
      <li><svg class="dot" viewBox="0 0 8 8"><circle cx="4" cy="4" r="4" fill="#1fa5dc"/><path d="M2.2 4.1 3.5 5.3 5.9 2.8" stroke="#121831" stroke-width="1.1" fill="none"/></svg>Easier to clean &amp; maintain</li>
    </ul>
  </section>

  <section class="room-panel abs">
    <div class="photo room-before" role="img" aria-label="Empty room with old worn floor before"></div>
    <div class="photo room-after" role="img" aria-label="Empty room with refinished floor after"></div>
  </section>
  <div class="tag before" style="left:655px; top:481px;">BEFORE</div>
  <div class="tag after" style="left:655px; top:953px;">AFTER</div>

  <div class="trust-title abs">PRACTICAL UPGRADES THAT PROTECT AND IMPROVE YOUR HOME</div>

  <div class="trust-item abs" style="left:26px;">
    <svg width="34" height="38" viewBox="0 0 34 38"><path d="M17 2 31 7v11c0 9-6 15-14 18C9 33 3 27 3 18V7z" fill="none" stroke="#d4831f" stroke-width="3"/><path d="M17 8 25 11v7c0 6-4 10-8 12z" fill="#d4831f"/></svg>
    Licensed &amp; Insured
  </div>
  <div class="trust-divider abs" style="left:205px;"></div>
  <div class="trust-item abs" style="left:211px;">
    <svg width="38" height="38" viewBox="0 0 38 38"><g stroke="#d4831f" stroke-width="4" stroke-linecap="round" fill="none"><path d="M9 29 27 11"/><path d="M10 9 29 29"/></g><circle cx="29" cy="8" r="6" fill="none" stroke="#d4831f" stroke-width="3"/><path d="M4 4 9 4 12 8 8 12 4 9z" fill="#d4831f"/></svg>
    Family-Owned<br>Local Business
  </div>
  <div class="trust-divider abs" style="left:383px;"></div>
  <div class="trust-item abs" style="left:394px;">
    <svg width="30" height="38" viewBox="0 0 30 38"><path d="M15 2C8 2 3 7 3 14c0 9 12 22 12 22s12-13 12-22C27 7 22 2 15 2z" fill="#d4831f"/><circle cx="15" cy="14" r="4.5" fill="#222c55"/></svg>
    Serving Prescott &amp;<br>Surrounding Areas
  </div>

  <div class="cta abs">
    <div class="label">CALL FOR A FREE ESTIMATE</div>
    <div class="phone">928-555-0147</div>
  </div>
  <div class="cta-note abs">Fast, professional service you can trust</div>

</main>
</body>
</html>
```